Gentle Harbor Label

We need labels for a new brewery called "Gentle Harbor":

We need one label, that we can slightly change to suit the style of liquid. So far the beers are:
- XPA
- Pale ALe
- IPA
- Black Ale

We want creative, fun labels, nothing traditional. but appropriate to suit all international markets.

Design was promoted in LOGO & not in Design, so we got a lot of logo's but very little designs for bottles/cans.

Gentle Harbor Brewing

```html
<!DOCTYPE html>
<html lang="en">
<head>
<meta charset="utf-8">
<title>Gentle Harbor Brewing – Label Range</title>
<link href="https://fonts.googleapis.com/css2?family=Barlow+Condensed:wght@400;600&display=swap" rel="stylesheet">
<style>
  :root {
    --backdrop: #ececec;
    --label-ink: #2a2d30;
    --label-edge: #34383b;
    --brand-teal: #93c6c4;
    --xpa-gold: #e6b82a;
    --pale-blue: #2c3d9c;
    --black-white: #f2f2f2;
  }
  * { margin: 0; padding: 0; box-sizing: border-box; }
  html, body {
    width: 1200px;
    height: 900px;
    overflow: hidden;
    background: var(--backdrop);
  }
  .label-range {
    width: 1200px;
    height: 900px;
    display: flex;
    justify-content: center;
    align-items: center;
    gap: 44px;
  }
  .label {
    width: 300px;
    height: 375px;
    background: var(--label-ink);
    border: 1px solid var(--label-edge);
    display: flex;
    flex-direction: column;
    align-items: center;
    justify-content: center;
    font-family: "Barlow Condensed", sans-serif;
  }
  .brand-name {
    color: var(--brand-teal);
    font-weight: 600;
    text-transform: uppercase;
    text-align: center;
    line-height: 1;
  }
  .brand-name .line-small {
    display: block;
    font-size: 40px;
    letter-spacing: 4px;
  }
  .brand-name .line-large {
    display: block;
    font-size: 64px;
    letter-spacing: 1px;
    margin-top: 4px;
  }
  .brand-name .line-tag {
    display: block;
    font-size: 17px;
    letter-spacing: 9px;
    margin-top: 8px;
    padding-left: 9px;
  }
  .style-name {
    margin-top: 54px;
    font-size: 32px;
    font-weight: 400;
    letter-spacing: 0.5px;
    text-transform: uppercase;
  }
  .style-black .style-name { color: var(--black-white); }
  .style-xpa .style-name { color: var(--xpa-gold); }
  .style-pale .style-name { color: var(--pale-blue); }
</style>
</head>
<body>
  <main class="label-range">
    <section class="label style-black">
      <h2 class="brand-name"><span class="line-small">Gentle</span><span class="line-large">Harbor</span><span class="line-tag">Brewing</span></h2>
      <p class="style-name">Black Ale</p>
    </section>
    <section class="label style-xpa">
      <h2 class="brand-name"><span class="line-small">Gentle</span><span class="line-large">Harbor</span><span class="line-tag">Brewing</span></h2>
      <p class="style-name">XPA</p>
    </section>
    <section class="label style-pale">
      <h2 class="brand-name"><span class="line-small">Gentle</span><span class="line-large">Harbor</span><span class="line-tag">Brewing</span></h2>
      <p class="style-name">Pale Ale</p>
    </section>
  </main>
</body>
</html>
```